Need Business Card for our Indian Grocery Store

Industry/Entity Type

Grocery Store

Contact Information for Business Card

Manoj Baweja
Director

Store Locations:

Willowmead
482 Elm Parade
P: 03 9172 5843

Ashbridge
613 Carlow Road
P: 03 9238 6014

email: kvtmarts@mailnest.example

Requirements
Must have
• Our logo Colours

```html
<!DOCTYPE html>
<html lang="en">
<head>
<meta charset="utf-8">
<title>KVT Marts – Business Card</title>
<link href="https://fonts.googleapis.com/css2?family=Roboto:wght@400;500;700;900&display=swap" rel="stylesheet">
<style>
  :root {
    --backdrop: #484647;
    --card: #f7f7f5;
    --brand-red: #e01f26;
    --ink: #111111;
  }
  * { margin: 0; padding: 0; box-sizing: border-box; }
  html, body {
    width: 1200px; height: 857px; overflow: hidden;
    background: var(--backdrop);
    font-family: "Roboto", Arial, sans-serif;
  }
  .stage { position: relative; width: 1200px; height: 857px; }
  .card {
    position: absolute;
    background: var(--card);
    border-radius: 12px;
    overflow: hidden;
  }
  .card--front { left: 31px; top: 276px; width: 559px; height: 319px; }
  .card--back { left: 608px; top: 272px; width: 563px; height: 320px; }

  .brand {
    position: absolute;
    display: flex; align-items: center; gap: 10px;
    color: var(--brand-red);
    font-weight: 700;
    white-space: nowrap;
  }
  .brand__square { width: 26px; height: 26px; background: var(--brand-red); }
  .card--front .brand { left: 24px; top: 110px; font-size: 44px; }
  .card--back .brand { left: 0; right: 0; top: 120px; justify-content: center; font-size: 50px; }
  .card--back .brand__square { width: 30px; height: 30px; }

  .email { position: absolute; color: var(--ink); font-size: 13.5px; letter-spacing: 0.8px; }
  .card--front .email { left: 20px; top: 224px; }
  .card--back .email { left: 0; right: 0; top: 281px; text-align: center; letter-spacing: 0.6px; }

  .person { position: absolute; left: 337px; top: 16px; }
  .person__name { font-weight: 900; font-size: 21.5px; letter-spacing: 1.8px; color: var(--ink); line-height: 1; }
  .person__role { font-weight: 700; font-size: 14.5px; letter-spacing: 1.2px; color: var(--brand-red); line-height: 1.2; }

  .locations { position: absolute; left: 338px; top: 132px; }
  .locations__heading { font-weight: 900; font-size: 17px; letter-spacing: 1.6px; color: var(--ink); line-height: 1; }
  .locations__heading--second { margin-top: 20px; }
  .store { color: var(--brand-red); font-weight: 500; font-size: 13px; letter-spacing: 1.4px; line-height: 19px; }
  .store--first { margin-top: 4px; }
  .store--second { margin-top: 8px; }

  .footer-band { position: absolute; left: 0; bottom: 0; width: 100%; height: 21px; background: var(--brand-red); }
  .footer-band svg { position: absolute; left: 262px; top: 0; }

  .footer-rules { position: absolute; left: 0; top: 299px; width: 100%; }
  .footer-rules span { display: block; height: 1.5px; background: var(--brand-red); opacity: 0.7; margin-bottom: 4.5px; }
</style>
</head>
<body>
<main class="stage">
  <section class="card card--front">
    <div class="brand"><span class="brand__square"></span>KVT Marts</div>
    <p class="email">email: kvtmarts@mailnest.example</p>

    <div class="person">
      <h1 class="person__name">MANOJ BAWEJA</h1>
      <p class="person__role">Director</p>
    </div>

    <div class="locations">
      <h2 class="locations__heading">STORE LOCATIONS :</h2>
      <div class="store store--first">
        <p>Willowmead</p>
        <p>482 Elm Parade</p>
        <p>03 9172 5843(P)</p>
      </div>
      <h2 class="locations__heading locations__heading--second">ASHBRIDGE :</h2>
      <div class="store store--second">
        <p>613 Carlow Road</p>
        <p>03 9238 6014(P)</p>
      </div>
    </div>

    <div class="footer-band">
      <svg width="40" height="21" viewBox="0 0 40 21">
        <g stroke="#111" stroke-width="1.6">
          <line x1="0" y1="21" x2="18" y2="0"/>
          <line x1="8" y1="21" x2="26" y2="0"/>
          <line x1="16" y1="21" x2="34" y2="0"/>
        </g>
      </svg>
    </div>
  </section>

  <section class="card card--back">
    <div class="brand"><span class="brand__square"></span>KVT Marts</div>
    <p class="email">email: kvtmarts@mailnest.example</p>
    <div class="footer-rules"><span></span><span></span></div>
  </section>
</main>
</body>
</html>
```